Varuko Business Card

I am looking for a business card design for a start-up company called Varuko Group. This is a management consultancy focused on sales, marketing, sales management, product management and AGILE software development. Our primary customers are $1M to $50M in revenue.

Varuko is the Italian word for "slope."

The path from $0 to $50M has many different growth stages associated with it. Each one having a significant slope to the next plateau. Our expertise helps our customers ascend each of those slopes. We bring experience, successful track-records in growing companies, best practices and a dive-in and roll-up your sleeves mentality. We are not sitting at base camp shouting instructions, we are right there with you, on the climb.

```html
<!DOCTYPE html>
<html lang="en">
<head>
<meta charset="utf-8">
<title>Varuko Business Card</title>
<link rel="stylesheet" href="https://fonts.googleapis.com/css2?family=Inter:wght@300;400&display=swap">
<style>
  :root {
    --backdrop: #d9dadb;
    --card: #eeeeee;
    --ink-grey: #4f5b64;
    --ink-soft: #6b757c;
    --brand-blue: #1583bf;
    --brand-blue-deep: #0f6aa0;
    --brand-green: #6aa531;
    --brand-green-deep: #4f8a24;
  }
  * { box-sizing: border-box; margin: 0; padding: 0; }
  html, body {
    width: 1200px;
    height: 900px;
    overflow: hidden;
    background: var(--backdrop);
    font-family: "Inter", "Helvetica Neue", Arial, sans-serif;
    font-weight: 300;
    color: var(--ink-grey);
  }
  .canvas {
    width: 1200px;
    height: 900px;
    display: flex;
    flex-direction: column;
    align-items: center;
    justify-content: center;
    gap: 50px;
  }
  .card {
    position: relative;
    width: 630px;
    height: 360px;
    background: var(--card);
    box-shadow: 0 2px 6px rgba(0, 0, 0, 0.12);
    overflow: hidden;
  }

  /* Front */
  .card-front .feature-panel {
    position: absolute;
    left: 0;
    top: 0;
    width: 330px;
    height: 100%;
    background: linear-gradient(160deg, var(--brand-blue-deep) 0%, var(--brand-blue) 35%, var(--brand-green) 65%, var(--brand-green-deep) 100%);
  }
  .card-front .brand-name {
    position: absolute;
    right: 40px;
    top: 112px;
    font-size: 66px;
    font-weight: 300;
    letter-spacing: -1px;
    line-height: 1;
    color: var(--ink-grey);
  }

  /* Back */
  .card-back .wordmark {
    position: absolute;
    left: 44px;
    top: 80px;
    display: flex;
    align-items: center;
    gap: 18px;
  }
  .card-back .brand-dot {
    width: 62px;
    height: 62px;
    border-radius: 50%;
    background: var(--brand-blue);
  }
  .card-back .brand-name {
    font-size: 82px;
    font-weight: 300;
    letter-spacing: -2px;
    line-height: 1;
    color: var(--ink-grey);
  }
  .holder {
    position: absolute;
    left: 48px;
    bottom: 64px;
  }
  .holder-name {
    font-size: 23px;
    font-weight: 300;
    letter-spacing: 0.5px;
    text-transform: uppercase;
    color: var(--ink-grey);
  }
  .holder-title {
    margin-top: 4px;
    font-size: 15px;
    color: var(--ink-soft);
  }
  .contact {
    position: absolute;
    left: 372px;
    top: 190px;
    display: grid;
    grid-template-columns: 48px auto;
    column-gap: 10px;
    row-gap: 3px;
    font-size: 12px;
    line-height: 1.35;
  }
  .contact dt { color: var(--brand-blue); }
  .contact dd { color: var(--ink-grey); }
  .contact .web { color: var(--brand-blue); }
</style>
</head>
<body>
<main class="canvas">
  <section class="card card-front" aria-label="Card front">
    <div class="feature-panel" role="img" aria-label="Large blue and green brand graphic"></div>
    <span class="brand-name">Varuko</span>
  </section>

  <section class="card card-back" aria-label="Card back">
    <div class="wordmark">
      <span class="brand-dot"></span>
      <span class="brand-name">Varuko</span>
    </div>
    <div class="holder">
      <p class="holder-name">Daniel Morrow</p>
      <p class="holder-title">Product Marketing Manager</p>
    </div>
    <dl class="contact">
      <dt>phone</dt><dd>555.210.4830</dd>
      <dt>fax</dt><dd>555.210.4831</dd>
      <dt>email</dt><dd>daniel@varuko.com</dd>
      <dt></dt><dd>420 Ridgeline Avenue, Suite 120,<br>Ashford, MA 01000</dd>
      <dt></dt><dd class="web">www.varuko.com</dd>
    </dl>
  </section>
</main>
</body>
</html>
```